Website Homepage re-design Project

I run a large format poster printing business & have a website hosted on zorvacart using one of their templates, http://www.brightprintsheets.co.uk
I am looking to update the home page to give it a more professional look, it must be clear for our clients to choose their poster type from the homepage
The design must contain the 5 poster type categories as well as most of the information above the poster categories, most of the text below the green "terms & conditions" footer can be left as it is as it's used for keywords, maybe just tidied up a bit
I would like to keep the customer reviews & sample posters on the home page along with the quick glance (fly-out) poster prices
I would also like the 4 step ordering process graphic updated, ie where it say "Select Poster Type" "Choose Poster Size" etc, there are 4 variations of this graphic which I will need to insert in their respective pages
If something can be done with the company name "Kestrel Prints & Sealers" that would be great.
I would prefer a design which shows all the information down to the section where it says "Order Your Poster Here" displayed on the screen when the page is loaded

```html
<!DOCTYPE html>
<html lang="en">
<head>
<meta charset="utf-8">
<title>Kestrel Prints &amp; Sealers – Poster Printing &amp; Laminating</title>
<link href="https://fonts.googleapis.com/css2?family=Arimo:wght@400;700&family=Source+Sans+3:wght@400;600&display=swap" rel="stylesheet">
<style>
:root{
  --dark:#24272e;
  --dark-2:#2e313a;
  --ink:#222;
  --text-grey:#555;
  --panel-white:#fff;
  --accent-red:#b83a3a;
  --link-grey:#444;
  --head-font:"Source Sans 3",Arial,sans-serif;
  --body-font:"Arimo",Arial,sans-serif;
}
*{box-sizing:border-box;margin:0;padding:0}
html,body{width:1034px;height:1200px;overflow:hidden}
body{position:relative;background:var(--dark);font-family:var(--body-font);color:var(--ink)}
.abs{position:absolute}

/* header */
.header{left:0;top:0;width:1034px;height:110px;background:linear-gradient(#2a2d34,#1e2026)}
.header-strip{left:18px;top:0;width:1016px;height:16px;background:#32353d}
.brand{left:83px;top:0;width:217px;height:105px;border-radius:0 0 6px 6px;background:linear-gradient(#f4f4f4,#cfcfcf);overflow:hidden}
.brand-bar{left:0;top:0;width:217px;height:18px;background:#bdbdbd}
.brand-name{left:0;top:28px;width:217px;text-align:center;font-family:var(--head-font);font-size:26px;line-height:32px;color:#3a3a3a}
.currency{left:775px;top:2px;font-size:11px;color:#fff}
.flag{top:2px;width:21px;height:12px;border:1px solid #888}
.login-title{left:719px;top:38px;font-size:14px;color:#fff}
.login-btn{top:62px;height:27px;border-radius:4px;background:linear-gradient(#fff,#d9d9d9);font-size:11px;color:#222;display:flex;align-items:center;justify-content:center}

/* hero */
.hero{left:0;top:110px;width:1034px;height:372px;background:linear-gradient(#d2d2d2,#f3f3f3 55%,#fff)}
.slider{left:68px;top:8px;width:679px;height:305px;border:3px solid #111;border-radius:5px;background:var(--panel-white)}
.slider-visual{left:82px;top:10px;width:280px;height:272px;border-radius:6px;background:linear-gradient(135deg,#e2e2e2,#b9b9b9 55%,#9a6a4a)}
.slider-caption{left:363px;top:146px;font-family:var(--head-font);font-size:21.5px;line-height:26px;color:#222;white-space:nowrap}
.slider-arrow{top:123px;width:27px;height:51px;background:#111;border-radius:3px;display:flex;align-items:center;justify-content:center}
.sample{left:757px;top:12px;width:212px;height:189px;border-radius:4px;background:linear-gradient(#e2e2e2,#a9a9a9)}
.sample-poster{left:28px;top:10px;width:150px;height:170px;background:linear-gradient(#dfe9f5,#9ebede);border:2px solid #2f6bb0}
.review{left:757px;top:205px;width:212px;height:103px;overflow:hidden;border-radius:4px;background:linear-gradient(#fafafa,#cfcfcf);padding:5px 6px 0 8px;font-size:10.8px;line-height:16.5px;color:#111}
.stars{display:inline-flex;vertical-align:-1px;margin-left:4px}

/* nav */
.nav{left:68px;top:322px;width:899px;height:46px;border-radius:4px;background:linear-gradient(#dcdcdc,#f9f9f9)}
.nav-item{top:13px;font-size:13px;color:#111}
.nav-home{left:9px;top:4px;width:91px;height:42px;border-radius:4px 4px 0 0;background:linear-gradient(#6a6d74,#1f2228);color:#fff;font-size:13px;display:flex;align-items:center;justify-content:center}

/* steps */
.steps{left:70px;top:500px;width:898px;height:163px;border-radius:5px 5px 0 0;background:linear-gradient(#ececec,#fff 40px)}
.steps-icon{left:22px;top:17px;width:13px;height:13px;border:2px solid #111;background:#fff}
.steps-title{left:57px;top:14px;font-family:var(--head-font);font-size:17px;color:#111}
.step{top:64px;width:149px;height:81px;border:1px solid #9a9a9a;border-radius:4px;background:linear-gradient(#fafafa,#cfcfcf)}
.step-num{left:14px;top:4px;font-size:15px;color:var(--accent-red)}
.step-visual{left:40px;top:6px;width:70px;height:48px;border-radius:4px}
.step-label{left:0;bottom:4px;width:100%;text-align:center;font-size:12.5px;color:#111}

/* categories */
.categories{left:70px;top:678px;width:898px;height:231px;border-radius:5px 5px 0 0;background:linear-gradient(#e4e4e4,#fff 30px)}
.cat{top:26px}
.cat-title{font-family:var(--head-font);font-weight:600;font-size:14.5px;line-height:17px;color:#111}
.cat-text{font-size:10.2px;line-height:16.7px;color:var(--text-grey)}

/* info footer */
.info{left:0;top:909px;width:1034px;height:210px;background:linear-gradient(#f6f6f7,#dcdde0)}
.discount-title{left:89px;top:38px;font-size:13px;letter-spacing:.3px;color:#333}
.discount-text{left:89px;top:61px;font-size:10px;line-height:17px;color:#444}
.keywords{left:89px;top:127px;font-size:10px;line-height:18.5px;color:var(--link-grey)}
.divider{left:695px;top:13px;height:187px;border-left:1px dotted #666}
.contact-title{left:746px;top:24px;font-family:var(--head-font);font-weight:600;font-size:16px;color:#111}
.contact-text{left:746px;top:57px;font-size:12px;line-height:19.5px;color:#222}

/* bottom */
.bottom{left:0;top:1119px;width:1034px;height:81px;background:var(--dark-2)}
.social{top:24px;width:32px;height:32px;border-radius:50%;background:#c9ccd2}
.bottom-links{left:418px;top:18px;font-size:11.5px;color:#fff;white-space:pre}
.copyright{left:425px;top:45px;font-size:11.5px;color:#fff}
</style>
</head>
<body>

<header class="abs header">
  <div class="abs header-strip"></div>
  <div class="abs brand">
    <div class="abs brand-bar"></div>
    <div class="abs brand-name">Kestrel Prints &amp;<br>Sealers</div>
  </div>
  <div class="abs currency">Select Currency :</div>
  <div class="abs flag" style="left:872px;background:#2a3f8f" role="img" aria-label="Euro currency flag"></div>
  <div class="abs flag" style="left:899px;background:#6c4f7a" role="img" aria-label="Pound currency flag"></div>
  <div class="abs flag" style="left:927px;background:#b96b72" role="img" aria-label="Dollar currency flag"></div>
  <div class="abs login-title">LOGIN</div>
  <div class="abs login-btn" style="left:713px;width:104px">EMAIL ADDRESS</div>
  <div class="abs login-btn" style="left:825px;width:76px">ORDER NO</div>
  <div class="abs login-btn" style="left:912px;width:64px">LOGIN</div>
</header>

<section class="abs hero">
  <div class="abs slider">
    <div class="abs slider-visual" role="img" aria-label="Large format roll laminator with a landscape poster feeding through"></div>
    <div class="abs slider-caption">Poster Printing &amp; Laminating</div>
    <div class="abs slider-arrow" style="left:1px">
      <svg width="8" height="10" viewBox="0 0 8 10"><path d="M6 1 2 5l4 4" fill="none" stroke="#fff" stroke-width="1.5"/></svg>
    </div>
    <div class="abs slider-arrow" style="left:645px">
      <svg width="8" height="10" viewBox="0 0 8 10"><path d="M2 1l4 4-4 4" fill="none" stroke="#fff" stroke-width="1.5"/></svg>
    </div>
  </div>
  <div class="abs sample">
    <div class="abs sample-poster" role="img" aria-label="Sample scientific research poster with charts"></div>
  </div>
  <div class="abs review">
    Reviewer :<br>
    Tidewater
    <svg class="stars" width="52" height="10" viewBox="0 0 52 10">
      <g fill="#e9c21c" stroke="#6a5300" stroke-width=".5">
        <path id="st" d="M5 .5l1.3 3 3.2.2-2.5 2 .8 3.1L5 7.1 2.2 8.8 3 5.7.5 3.7l3.2-.2z"/>
        <use href="#st" x="10.5"/><use href="#st" x="21"/><use href="#st" x="31.5"/><use href="#st" x="42"/>
      </g>
    </svg><br>
    I've just received my order and have to<br>say it's FANTASTIC! The quality, colours<br>and delivery time are exceptional, I will<br>probably be making multiple.
  </div>
  <nav class="abs nav">
    <div class="abs nav-home">Home</div>
    <span class="abs nav-item" style="left:113px">About Us</span>
    <span class="abs nav-item" style="left:206px">Contact Us</span>
    <span class="abs nav-item" style="left:306px">FAQ</span>
    <span class="abs nav-item" style="left:367px">Colour Calibration</span>
    <span class="abs nav-item" style="left:506px">Customer Comments</span>
    <span class="abs nav-item" style="left:665px">Search</span>
    <span class="abs nav-item" style="left:741px">View Cart</span>
  </nav>
</section>

<section class="abs steps">
  <div class="abs steps-icon"></div>
  <div class="abs steps-title">Follow These Steps</div>
  <div class="abs step" style="left:51px">
    <span class="abs step-num">1</span>
    <div class="abs step-visual" style="background:linear-gradient(#cfd3d8,#6f757d)" role="img" aria-label="Wide format printer"></div>
    <div class="abs step-label">Poster Type</div>
  </div>
  <div class="abs step" style="left:242px">
    <span class="abs step-num">2</span>
    <div class="abs step-visual" style="background:linear-gradient(#e6e1d6,#7a6e62)" role="img" aria-label="Stack of printed posters in various sizes"></div>
    <div class="abs step-label">Choose Poster Size</div>
  </div>
  <div class="abs step" style="left:434px">
    <span class="abs step-num">3</span>
    <div class="abs step-visual" style="background:linear-gradient(#b6a58a,#3a3a3a)" role="img" aria-label="Photo printer outputting a picture"></div>
    <div class="abs step-label">Upload Your File</div>
  </div>
  <div class="abs step" style="left:653px">
    <span class="abs step-num">4</span>
    <div class="abs step-visual" style="background:linear-gradient(#d9b48c,#6d5a43)" role="img" aria-label="Hand holding payment cards"></div>
    <div class="abs step-label">Pay for Poster</div>
  </div>
</section>

<section class="abs categories">
  <div class="abs cat" style="left:32px;width:140px">
    <div class="cat-title">Matt Photo Paper</div>
    <p class="cat-text" style="margin-top:19px">Photo Quality Poster printing,<br>Printed at 2400 dpi on 180<br>gsm Silk Matt Photo paper,<br>perfect for high quality<br>presentations &amp; matt photo<br>reproduction, these poster<br>will show the finest details</p>
  </div>
  <div class="abs cat" style="left:190px;width:145px">
    <div class="cat-title">Gloss Photo Paper</div>
    <p class="cat-text" style="margin-top:19px">Photo Quality Poster Printing,<br>Printed at 2400 dpi on 190<br>gsm Gloss Photo paper,<br>perfect for high quality<br>presentations &amp; photographic<br>prints with vivid true to life<br>colours.</p>
  </div>
  <div class="abs cat" style="left:348px;width:155px">
    <div class="cat-title">Budget Posters Student Presentation Poster</div>
    <p class="cat-text" style="margin-top:3px">Photo Quality Poster Printing,<br>Printed at 1200dpi on 170gsm<br>High Resolution coated paper,<br>this printing option is ideally<br>suited to students presentations</p>
  </div>
  <div class="abs cat" style="left:524px;width:160px">
    <div class="cat-title">Poster with Gloss<br>Encapsulating</div>
    <p class="cat-text" style="margin-top:6px">Photo Quality Poster printing &amp;<br>Laminating. Printed at 2400 dpi<br>&amp; Laminated on both sides with<br>a 5mm edge seal, the Gloss<br>finish enhances the colours.<br>Weatherproof &amp; durable, these<br>posters are ideal for long term use</p>
  </div>
  <div class="abs cat" style="left:701px;width:190px">
    <div class="cat-title">Poster with Matt<br>Encapsulating</div>
    <p class="cat-text" style="margin-top:8px">Photo Quality Poster printing &amp;<br>Laminating. Printed at 2400dpi &amp;<br>Laminated on both sides with a 5mm<br>edge seal, the Matt finish reduces light<br>reflection. Weatherproof &amp; durable,<br>these posters are ideal for long term use</p>
  </div>
</section>

<section class="abs info">
  <div class="abs discount-title">STUDENT DISCOUNT</div>
  <p class="abs discount-text">10% Off all Encapsulated Posters<br>The discount only applies to Posters that are encapsulated with either Gloss or Matt film<br>The Student Discount refund is issued shortly after payment is received</p>
  <p class="abs keywords">
    Thornfield College | Regent Institute | Health Trust | Aldgate Clinic | Marlow Hospital | University Students | Elective Posters<br>
    A0 Printing | A1 Printing | printing of poster | poster printing<br>
    A0 Posters | A1 Posters | A2 Posters | A0 Laminating | A1 Laminating | A2 laminating<br>
    Full Colour Scientific Posters | Encapsulated Posters | Laminated posters | poster printing | Conference Posters
  </p>
  <div class="abs divider"></div>
  <div class="abs contact-title">CONTACT</div>
  <p class="abs contact-text">A0 Poster Printing &amp; A1 Poster Printing &amp;<br>Laminating Prices<br>Kestrel Prints &amp; Sealers<br>Central London, Wales, Scotland, UK.<br>tel: 01632 960418<br>mob: 07700 900 615</p>
</section>

<footer class="abs bottom">
  <div class="abs social" style="left:99px" aria-label="Social link"></div>
  <div class="abs social" style="left:148px" aria-label="Social link"></div>
  <div class="abs social" style="left:197px" aria-label="News feed link"></div>
  <div class="abs bottom-links">Terms &amp; Conditions       |       Privacy    |    Sitemap      |      Contact us</div>
  <div class="abs copyright">Copyright © 2012 Kestrel Prints &amp; Sealers, All Rights Reserved</div>
</footer>

</body>
</html>
```